Presentation Folder with inside Pockets

We need a Presentation Folder with inside pockets. The size of the folder will be 9" x 12" and will be printed on the cover, the back and the inside folder flaps. The design will be very simple and consist of our logo (large) on the front cover and our logo (smaller) and contact information on the back. We are open to various colors that you think may go along with our logo. When you display your work, show the front, back and inside.

Target Market(s)

Pharmaceutical Companies

Industry/Entity Type

Work

Requirements
Should not have
• please do not add stock medical photos.

```html
<!DOCTYPE html>
<html lang="en">
<head>
<meta charset="utf-8">
<title>Meridian Trial Works – Presentation Folder</title>
<link href="https://fonts.googleapis.com/css2?family=Arimo:wght@400;700&display=swap" rel="stylesheet">
<style>
  :root{
    --bg:#c9c9c9;
    --paper:#ffffff;
    --paper-shade:#eeeeee;
    --blue:#0a6fb8;
    --blue-dark:#064f8c;
    --blue-light:#1a8ad0;
    --green:#72bd44;
    --green-dark:#4e8a34;
    --ink:#1d1d1d;
    --muted:#333333;
  }
  html,body{margin:0;padding:0;}
  body{
    width:1129px;height:1200px;overflow:hidden;
    background:var(--bg);
    font-family:"Arimo",Arial,sans-serif;
    position:relative;
  }
  .spread{position:absolute;display:flex;box-shadow:0 6px 18px rgba(0,0,0,.25);}
  .spread--inside{left:234px;top:50px;}
  .spread--outside{left:184px;top:560px;}
  .panel{display:block;background:var(--paper);}
  .spread--inside .panel{width:330px;height:440px;}
  .spread--outside .panel{width:380px;height:507px;}
  .panel + .panel{border-left:1px solid #d8d8d8;}
  .brand-name{font-family:"Arimo",Arial,sans-serif;font-weight:700;fill:var(--ink);}
  .contact{font-family:"Arimo",Arial,sans-serif;font-weight:400;fill:var(--muted);font-size:5.4px;}
</style>
</head>
<body>

<div class="spread spread--inside">
  <svg class="panel panel--inside-left" viewBox="0 0 300 400" preserveAspectRatio="none">
    <rect width="300" height="400" fill="var(--paper)"/>
    <path d="M0,292 L300,272 L300,280 L0,300Z" fill="var(--paper-shade)"/>
    <path d="M0,300 L300,280 L300,400 L0,400Z" fill="var(--paper)"/>
    <path d="M0,330 C90,300 200,312 300,350 L300,400 L0,400Z" fill="var(--blue)"/>
    <path d="M110,400 C180,360 250,350 300,352 L300,360 C250,362 190,372 140,400Z" fill="var(--blue-dark)"/>
    <path d="M0,330 C90,300 200,312 300,350 L300,356 C200,320 90,310 0,338Z" fill="var(--blue-light)"/>
    <path class="card-slot" d="M100,318 L170,306 L176,312 L182,348 L178,354 L108,366 L102,360 L96,324Z" fill="var(--paper)"/>
  </svg>
  <svg class="panel panel--inside-right" viewBox="0 0 300 400" preserveAspectRatio="none">
    <rect width="300" height="400" fill="var(--paper)"/>
    <path d="M0,272 L300,292 L300,300 L0,280Z" fill="var(--paper-shade)"/>
    <path d="M0,280 L300,300 L300,400 L0,400Z" fill="var(--paper)"/>
    <path d="M0,280 L150,290 C200,320 250,360 300,400 L0,400Z" fill="var(--blue)"/>
    <path d="M0,340 C80,360 180,380 230,400 L0,400Z" fill="var(--blue-dark)"/>
    <path class="card-slot" d="M70,326 L140,314 L146,320 L152,356 L148,362 L78,374 L72,368 L66,332Z" fill="var(--paper)"/>
    <circle cx="203" cy="301" r="3.6" fill="var(--green)"/>
    <text class="brand-name" x="210" y="304" font-size="6.5">MERIDIAN TRIAL WORKS</text>
    <text class="brand-name" x="250" y="311" font-size="4.5" text-anchor="middle">INC.</text>
  </svg>
</div>

<div class="spread spread--outside">
  <svg class="panel panel--back" viewBox="0 0 300 400" preserveAspectRatio="none">
    <rect width="300" height="400" fill="var(--paper)"/>
    <path d="M0,0 L24,0 C30,230 150,330 300,372 L300,392 L0,392Z" fill="var(--green)"/>
    <path d="M24,0 L30,0 C36,228 158,326 300,366 L300,372 C150,330 30,230 24,0Z" fill="var(--green-dark)"/>
    <path d="M0,348 C70,362 130,378 170,392 L300,392 L300,400 L0,400Z" fill="var(--paper)"/>
    <path d="M0,360 C50,372 100,388 130,400 L0,400Z" fill="var(--blue-dark)"/>
    <circle cx="102" cy="196" r="5" fill="var(--green)"/>
    <text class="brand-name" x="111" y="199" font-size="8">MERIDIAN TRIAL WORKS</text>
    <line x1="111" y1="205" x2="150" y2="205" stroke="var(--ink)" stroke-width=".6"/>
    <text class="brand-name" x="162" y="207" font-size="5.5" text-anchor="middle">INC.</text>
    <line x1="174" y1="205" x2="213" y2="205" stroke="var(--ink)" stroke-width=".6"/>
    <text class="contact" x="138" y="300" text-anchor="middle">Meridian Trial Works, Inc.</text>
    <text class="contact" x="138" y="307" text-anchor="middle">120 Linden Avenue</text>
    <text class="contact" x="138" y="314" text-anchor="middle">Fairview, NY 11000</text>
    <text class="contact" x="138" y="326" text-anchor="middle">Tel: +1-555-014-2290</text>
    <text class="contact" x="138" y="333" text-anchor="middle">Email: hello@meridiantw.example</text>
    <text class="contact" x="138" y="340" text-anchor="middle">Web: www.meridiantw.example</text>
  </svg>
  <svg class="panel panel--front" viewBox="0 0 300 400" preserveAspectRatio="none">
    <rect width="300" height="400" fill="var(--paper)"/>
    <path d="M300,260 C270,330 210,380 150,400 L300,400Z" fill="var(--blue-light)"/>
    <path d="M300,240 C285,300 250,350 210,380 L228,378 C262,350 290,310 300,276Z" fill="var(--blue-dark)"/>
    <circle cx="40" cy="200" r="12" fill="var(--green)"/>
    <text class="brand-name" x="60" y="206" font-size="14.5">MERIDIAN TRIAL</text>
    <text class="brand-name" x="60" y="224" font-size="14.5">WORKS</text>
    <line x1="125" y1="220" x2="175" y2="220" stroke="var(--ink)" stroke-width=".8"/>
    <text class="brand-name" x="190" y="224" font-size="9" text-anchor="middle">INC.</text>
    <line x1="205" y1="220" x2="270" y2="220" stroke="var(--ink)" stroke-width=".8"/>
  </svg>
</div>

</body>
</html>
```